Calibrated NET Systems
Business card and Stationary
Project: Calibrated NET Systems
Calibrated NET Systems - Information Technology
Creative Brief
Professional
Dean Harlowe
Technical Consultant
Please leave the address part blank.
dean.harlowe@calnet.ca
www.calnet.ca

```html
<!DOCTYPE html>
<html lang="en">
<head>
<meta charset="utf-8">
<title>Calibrated NET Systems – Stationery</title>
<link href="https://fonts.googleapis.com/css2?family=Open+Sans:wght@400;600;700&display=swap" rel="stylesheet">
<style>
:root{
  --navy:#0d2a4e;
  --blue:#1f8fd1;
  --sky:#5fc3ef;
  --ink:#2b2f36;
  --muted:#7a828c;
  --paper:#ffffff;
  --stage:#e9e6e1;
  --rule:#c9ced4;
  --ghost:#eef2f6;
}
*{box-sizing:border-box;margin:0;padding:0}
html,body{width:1200px;height:559px;overflow:hidden}
body{background:var(--stage);font-family:"Open Sans",Arial,sans-serif;color:var(--ink);position:relative}
.piece-label{position:absolute;font-size:7px;font-weight:600;color:var(--ink);text-align:center}
.sheet{position:absolute;background:var(--paper);box-shadow:0 2px 6px rgba(0,0,0,.25);overflow:hidden}
.wave{position:absolute;left:0;top:0;width:100%}
.brand{position:absolute;display:flex;align-items:center;gap:4px}
.brand-mark{background:var(--blue);flex:none}
.brand-name{color:var(--blue);font-weight:600;white-space:nowrap}
.ghost-mark{position:absolute;background:var(--ghost);border-radius:8px}
/* fax */
.fax{left:43px;top:19px;width:336px;height:523px}
.fax-title{position:absolute;right:22px;top:104px;font-size:9px;font-weight:700;color:var(--navy)}
.fax-table{position:absolute;left:18px;top:116px;width:300px;border-collapse:collapse;font-size:6px}
.fax-table td{border:1px solid var(--rule);height:15px;padding:0 4px}
.fax-table .field{width:45px;color:var(--muted)}
.checks{position:absolute;left:18px;top:188px;display:flex;gap:14px;font-size:5.5px;color:var(--muted)}
.checks span::before{content:"";display:inline-block;width:6px;height:6px;border:1px solid var(--muted);margin-right:3px;vertical-align:-1px}
.footer{position:absolute;bottom:9px;left:0;width:100%;text-align:center;font-size:5px;color:var(--muted);word-spacing:2px}
.footer b{color:var(--blue);font-weight:700}
/* letterhead */
.letterhead{left:408px;top:19px;width:336px;height:523px}
/* cards */
.card{width:182px;height:108px;top:36px}
.card-front{left:773px}
.card-back{left:965px;border-radius:8px}
.card-person{position:absolute;right:10px;top:14px;text-align:right;font-size:5px;color:var(--muted);line-height:1.35}
.card-person strong{display:block;font-size:6.5px;color:var(--ink)}
.partner-badge{position:absolute;right:10px;top:62px;width:34px;height:16px;background:#d9dde2;border-radius:2px}
.card-contact{position:absolute;left:10px;bottom:8px;font-size:4.5px;color:var(--muted);line-height:1.4}
/* envelopes */
.env-front{left:773px;top:156px;width:379px;height:137px}
.env-back{left:773px;top:355px;width:379px;height:168px}
</style>
</head>
<body>

<div class="piece-label" style="left:43px;top:5px;width:336px">Fax Cover</div>
<section class="sheet fax">
  <svg class="wave" height="90" viewBox="0 0 336 90" preserveAspectRatio="none" aria-hidden="true">
    <path d="M0 0H336V58C250 40 140 50 0 80Z" fill="var(--navy)"/>
    <path d="M0 80C140 50 250 40 336 58V64C250 48 150 58 0 88Z" fill="var(--sky)"/>
  </svg>
  <div class="brand" style="left:18px;top:32px"><span class="brand-mark" style="width:14px;height:14px"></span><span class="brand-name" style="font-size:11px">Calibrated NET Systems</span></div>
  <div class="fax-title">FAX</div>
  <table class="fax-table">
    <tr><td class="field">To:</td><td></td><td class="field">From:</td><td></td></tr>
    <tr><td class="field">Fax:</td><td></td><td class="field">Pages:</td><td></td></tr>
    <tr><td class="field">Phone:</td><td></td><td class="field">Date:</td><td></td></tr>
    <tr><td class="field">Re:</td><td></td><td class="field">CC:</td><td></td></tr>
  </table>
  <div class="checks"><span>Urgent</span><span>For Review</span><span>Please Comment</span><span>Please Reply</span><span>Please Recycle</span></div>
  <div class="ghost-mark" style="left:90px;top:250px;width:150px;height:200px"></div>
  <p class="footer"><b>P</b> +1 905 555 0148 <b>F</b> +1 905 555 0149 <b>E</b> dean.harlowe@calnet.ca <b>W</b> www.calnet.ca</p>
</section>

<div class="piece-label" style="left:408px;top:5px;width:336px">Letterhead</div>
<section class="sheet letterhead">
  <svg class="wave" height="90" viewBox="0 0 336 90" preserveAspectRatio="none" aria-hidden="true">
    <path d="M0 0H336V58C250 40 140 50 0 80Z" fill="var(--navy)"/>
    <path d="M0 80C140 50 250 40 336 58V64C250 48 150 58 0 88Z" fill="var(--sky)"/>
  </svg>
  <div class="ghost-mark" style="left:90px;top:250px;width:150px;height:200px"></div>
  <p class="footer"><b>P</b> +1 905 555 0148 <b>F</b> +1 905 555 0149 <b>E</b> dean.harlowe@calnet.ca <b>W</b> www.calnet.ca</p>
</section>

<div class="piece-label" style="left:773px;top:22px;width:182px">Business Card (Front)</div>
<section class="sheet card card-front">
  <svg class="wave" height="34" viewBox="0 0 182 34" preserveAspectRatio="none" aria-hidden="true">
    <path d="M0 0H182V14C120 8 60 16 0 30Z" fill="var(--navy)"/>
    <path d="M0 30C60 16 120 8 182 14V17C120 11 60 20 0 34Z" fill="var(--sky)"/>
  </svg>
  <div class="brand" style="left:10px;top:38px"><span class="brand-mark" style="width:8px;height:8px"></span><span class="brand-name" style="font-size:6px">Calibrated NET Systems</span></div>
  <div class="card-person"><strong>Dean Harlowe</strong>Technical Consultant</div>
  <div class="partner-badge" role="img" aria-label="Partner badge"></div>
  <div class="card-contact">P +1 905 555 0148 · F +1 905 555 0149<br>dean.harlowe@calnet.ca · www.calnet.ca</div>
</section>

<div class="piece-label" style="left:965px;top:22px;width:182px">Business Card (Back)</div>
<section class="sheet card card-back">
  <div class="brand" style="left:76px;top:38px"><span class="brand-mark" style="width:30px;height:30px"></span></div>
</section>

<section class="sheet env-front">
  <svg class="wave" height="48" viewBox="0 0 379 48" preserveAspectRatio="none" aria-hidden="true">
    <path d="M0 0H379V22C250 12 120 22 0 42Z" fill="var(--navy)"/>
    <path d="M0 42C120 22 250 12 379 22V26C250 16 120 27 0 48Z" fill="var(--sky)"/>
  </svg>
  <div class="brand" style="left:14px;top:50px"><span class="brand-mark" style="width:14px;height:14px"></span><span class="brand-name" style="font-size:11px">Calibrated NET Systems</span></div>
</section>

<div class="piece-label" style="left:773px;top:341px;width:379px">Envelope (back)</div>
<section class="sheet env-back">
  <svg width="379" height="168" viewBox="0 0 379 168" aria-hidden="true">
    <path d="M0 0L189 78L379 0" fill="#f7f8fa" stroke="var(--rule)" stroke-width="1"/>
    <path d="M0 168L160 70M379 168L219 70" stroke="var(--rule)" stroke-width="1" fill="none"/>
  </svg>
  <p class="footer" style="bottom:14px">www.calnet.ca</p>
</section>

</body>
</html>
```